Stationary Package for New Bookkeeping Business

We need the following stationary designs:

- Business Card
- Letterhead
- With Comps
- Envelopes
- Paper Folder
- Email Signature

We will provide accounting and bookkeeping services to small business. We would like have the main color as blue and have a modern professional look.

Variations of colour and shades of blue welcome
Preference for deeper darker blue - navy

Variations of font in logo also welcome

Requirements
Must have
• Rosalind
B.Bus (Accounting)
Registered BAS Agent

Phone 0491 382 507
Post PO Box 947 Kelmora NSW 2768

Email rosalind@tarwinledgers.com

Business Card to be bold and eye catching

Should not have
• Letter head to not have too much colour on it

```html
<!DOCTYPE html>
<html lang="en">
<head>
<meta charset="utf-8">
<title>Tarwin Ledgers – Business Card</title>
<link href="https://fonts.googleapis.com/css2?family=Questrial&family=Arimo:wght@400&display=swap" rel="stylesheet">
<style>
  :root {
    --backdrop: #0a78b8;
    --navy: #2b2f45;
    --navy-pattern: #31385a;
    --card-white: #eeeeee;
    --mark-grey: #9a9a9a;
    --text-grey: #6c6c6c;
    --rule-grey: #555555;
    --light-text: #e6e6e6;
    --rule-light: #c8c8c8;
  }
  * { margin: 0; padding: 0; box-sizing: border-box; }
  html, body {
    width: 1200px; height: 900px; overflow: hidden;
    background: var(--backdrop);
  }
  .stage { position: relative; width: 1200px; height: 900px; }

  .card {
    position: absolute; left: 355px; width: 487px; height: 271px; overflow: hidden;
  }
  .card--front { top: 157px; background: var(--navy); }
  .card--back { top: 467px; background: var(--card-white); }

  .front-pattern {
    position: absolute; inset: 0;
    background: linear-gradient(180deg, var(--navy-pattern), var(--navy) 85%);
  }
  .front-rule {
    position: absolute; left: 0; top: 198px; width: 143px; height: 1px;
    background: var(--rule-light);
  }
  .brand { position: absolute; display: flex; align-items: center; }
  .brand-square { background: var(--mark-grey); flex: none; }
  .brand-name {
    font-family: "Questrial", sans-serif; line-height: 0.95; letter-spacing: -0.5px;
  }
  .card--front .brand { left: 150px; top: 163px; }
  .card--front .brand-square { width: 67px; height: 67px; margin-right: 14px; }
  .card--front .brand-name { font-size: 38px; color: var(--light-text); }

  .card--back .brand { left: 32px; top: 28px; }
  .card--back .brand-square { width: 70px; height: 70px; margin-right: 14px; }
  .card--back .brand-name { font-size: 40px; color: var(--navy); }

  .details {
    position: absolute; left: 117px; font-family: "Arimo", sans-serif; color: var(--text-grey);
  }
  .holder { top: 129px; }
  .holder-name { font-size: 17px; line-height: 20px; }
  .holder-role { font-size: 12.5px; color: var(--navy); line-height: 18px; letter-spacing: 0.2px; }
  .holder-email { font-size: 12.5px; margin-top: 8px; }
  .label { color: var(--navy); }
  .back-rule {
    position: absolute; left: 0; top: 197px; width: 451px; height: 1px; background: var(--rule-grey);
  }
  .contact { top: 209px; font-size: 12.5px; line-height: 16px; }
  .web { color: var(--navy); letter-spacing: 1px; }
</style>
</head>
<body>
<main class="stage">
  <section class="card card--front">
    <div class="front-pattern" role="img" aria-label="Repeating pattern of small plus, percent, dollar and tick symbols in muted navy"></div>
    <div class="front-rule"></div>
    <div class="brand">
      <span class="brand-square"></span>
      <span class="brand-name">Tarwin<br>Ledgers</span>
    </div>
  </section>

  <section class="card card--back">
    <div class="brand">
      <span class="brand-square"></span>
      <span class="brand-name">Tarwin<br>Ledgers</span>
    </div>
    <div class="details holder">
      <p class="holder-name">Rosalind B.Bus (Accounting)</p>
      <p class="holder-role">REGISTERED BAS AGENT</p>
      <p class="holder-email"><span class="label">E</span> rosalind@tarwinledgers.com</p>
    </div>
    <div class="back-rule"></div>
    <div class="details contact">
      <p><span class="label">T</span> 0491 382 507</p>
      <p>Post PO Box 947 Kelmora NSW 2768</p>
      <p class="web">www.tarwinledgers.com</p>
    </div>
  </section>
</main>
</body>
</html>
```